Sleek business card design for digital agency.

Brief document attached for detailed description and inspiration. Looking for a minimalist sleek, cool, modern business card design.

Industry/Entity Type

Digital

```html
<!DOCTYPE html>
<html lang="en">
<head>
<meta charset="utf-8">
<title>Business Card – Daniel Hartley</title>
<link rel="stylesheet" href="https://fonts.googleapis.com/css2?family=Open+Sans:wght@400;700&display=swap">
<style>
  :root {
    --backdrop: #3b3b3d;
    --card: #1c1c1e;
    --ink: #f2f2f2;
    --accent: #1ea0e6;
    --art-light: rgba(200, 200, 205, 0.22);
    --art-dark: rgba(28, 28, 30, 0);
  }
  html, body {
    margin: 0;
    width: 1200px;
    height: 900px;
    overflow: hidden;
    background: var(--backdrop);
  }
  .canvas {
    position: relative;
    width: 1200px;
    height: 900px;
    display: flex;
    align-items: center;
    justify-content: center;
  }
  .card {
    position: relative;
    width: 990px;
    height: 605px;
    background: var(--card);
    box-shadow: 0 18px 40px rgba(0, 0, 0, 0.45);
    overflow: hidden;
    font-family: "Open Sans", sans-serif;
    color: var(--ink);
  }
  .contact {
    position: absolute;
    left: 120px;
    top: 70px;
    font-size: 21px;
    line-height: 1.32;
  }
  .contact p { margin: 0; }
  .name {
    color: var(--accent);
    font-weight: 700;
  }
  .details {
    margin-top: 34px !important;
  }
  .line {
    display: flex;
    align-items: center;
    gap: 10px;
  }
  .icon {
    width: 18px;
    height: 18px;
    fill: var(--accent);
    flex: none;
  }
  .social { margin-top: 18px !important; }
  .address { margin-top: 18px !important; }
  .artwork {
    position: absolute;
    right: 0;
    bottom: 0;
    width: 500px;
    height: 340px;
    background: radial-gradient(ellipse at 60% 60%, var(--art-light), var(--art-dark) 70%);
  }
</style>
</head>
<body>
<main class="canvas">
  <section class="card">
    <div class="contact">
      <p class="name">Daniel Hartley</p>
      <p class="role">Marketing Director</p>
      <p class="drink">Drink order: G&amp;T with cucumber</p>

      <div class="details">
        <p class="line">
          <svg class="icon" viewBox="0 0 20 20" aria-hidden="true"><path d="M1 4h18v12H1z M1 4l9 7 9-7" fill="none" stroke="var(--accent)" stroke-width="0"/><path d="M1 4h18L10 11z M1 6v10h18V6l-9 7z"/></svg>
          dhartley@flintworks.com
        </p>
        <p class="line">
          <svg class="icon" viewBox="0 0 20 20" aria-hidden="true"><path d="M6 1h8a1.5 1.5 0 0 1 1.5 1.5v15A1.5 1.5 0 0 1 14 19H6a1.5 1.5 0 0 1-1.5-1.5v-15A1.5 1.5 0 0 1 6 1zm0 2v12h8V3zm4 13a1 1 0 1 0 0 2 1 1 0 0 0 0-2z"/></svg>
          0412 555 018
        </p>
        <p class="line">
          <svg class="icon" viewBox="0 0 20 20" aria-hidden="true"><path d="M4 1l4 4-2 3c1 2.5 3.5 5 6 6l3-2 4 4-3 3C9 19 1 11 1 4z"/></svg>
          03 9000 1234
        </p>
      </div>

      <p class="social">@dhartley82<br>facebook.com/FlintWorks</p>
      <p class="address">Level 2, 18 Carden St<br>East Halford NSW 2999</p>
    </div>

    <div class="artwork" role="img" aria-label="Silver and gloss line illustration of a crustacean claw and feathered tail"></div>
  </section>
</main>
</body>
</html>
```